Facebook post for announcing the new company's website design

Need a facebook post (English language) for announcing that the company has a renovated website:
https://www.clinivostaremoto.com/en/

The website existed already but received recently a brand new design: more light, modern and sophisticated.

Please find as an attachment source files of our logo so that you can provide the best quality, thanks.

Also you may find our facebook page at:
https://pt-pt.facebook.com/clinivostaremoto/

Target Market(s)

Facebook audience

Colors

Designer to choose colors to be used in the design.

Requirements
Must have
• Our website has a new design!
• www.clinivostaremoto.com
Nice to have
• The post should feel as somehow connected to the website. Please check our above mentioned website, things should be related. For instance, use our logo (check attached files).
• You may also use this opportunity to remind the audience about our business core messages: excellency, quality, safety.

```html
<!DOCTYPE html>
<html lang="en">
<head>
<meta charset="utf-8">
<title>Clinivosta Remoto – Our website has a new design</title>
<link rel="stylesheet" href="https://fonts.googleapis.com/css2?family=Open+Sans:wght@300;400&display=swap">
<style>
  :root {
    --stage: #1a1a1a;
    --wall: #c8ccd1;
    --wall-light: #dfe2e5;
    --paint: #3f809f;
    --paint-deep: #36708c;
    --band: #1a6f9b;
    --white: #ffffff;
    --illustration-strong: rgba(255,255,255,0.30);
    --illustration-soft: rgba(255,255,255,0.08);
  }
  * { box-sizing: border-box; margin: 0; padding: 0; }
  html, body { width: 1200px; height: 753px; overflow: hidden; background: var(--stage); }
  body { position: relative; font-family: "Open Sans", Arial, sans-serif; }

  .cover {
    position: absolute; left: 40px; top: 164px;
    width: 1121px; height: 426px; overflow: hidden;
  }
  .cover__wall {
    position: absolute; inset: 0;
    background: linear-gradient(180deg, var(--wall-light), var(--wall));
  }
  .cover__paint {
    position: absolute; left: 18px; top: 31px; width: 1085px; height: 371px;
    background: linear-gradient(160deg, var(--paint), var(--paint-deep));
  }
  .cover__illustration {
    position: absolute; left: 841px; top: 98px; width: 280px; height: 328px;
    border-radius: 40px 0 0 0;
    background: linear-gradient(200deg, var(--illustration-strong), var(--illustration-soft));
  }
  .cover__headline {
    position: absolute; left: 76px; top: 80px;
    color: var(--white); font-weight: 300; font-size: 42px; line-height: 52px;
  }
  .brand {
    position: absolute; left: 64px; top: 228px;
    display: flex; align-items: center; gap: 14px;
  }
  .brand__mark { width: 60px; height: 60px; background: var(--white); }
  .brand__name { color: var(--white); font-weight: 400; font-size: 34px; line-height: 1; }
  .cover__url {
    position: absolute; left: 0; top: 338px; width: 459px; height: 42px;
    background: var(--band); color: var(--white);
    font-weight: 300; font-size: 25px; line-height: 42px; padding-left: 78px;
  }
</style>
</head>
<body>
  <section class="cover">
    <div class="cover__wall" role="img" aria-label="Light grey painted brick wall texture"></div>
    <div class="cover__paint" role="img" aria-label="Brick wall brushed over with teal blue paint"></div>
    <div class="cover__illustration" role="img" aria-label="White line illustration of a megaphone"></div>
    <h1 class="cover__headline">Our website<br>has a new design!</h1>
    <div class="brand">
      <span class="brand__mark"></span>
      <span class="brand__name">Clinivosta Remoto</span>
    </div>
    <p class="cover__url">www.clinivostaremoto.com</p>
  </section>
</body>
</html>
```